Business Goals Posters for display within company office and factory.

We have three (3) high level business goals we want to display in the office and factory areas of the business.

1. Under the heading of "QUALITY"
"We will have pride and ownership of every product and service delivered to our customers."

2. Under the heading of "PRODUCTIVITY"
"We will put the customer's expectations first and ensure our team is empowered to do so."

3. Under the heading of "SAFETY"
"We will shift our culture to ensure safety is our first thought on every job."

We would like a matching set of posters with these three headings and statements with a background suitable for display in a business environment. The posters will be displayed in sizes from A4 and A2.
The company's logo is Red and Black (see attachment) .
We make Electric and Hydraulic power packs for industrial market.
our website will give you an idea of what we do www.tarnwickdrives.com.au

Industry/Entity Type

Power Generation

Colors

Designer to choose colors to be used in the design.

Requirements
Must have
• The posters must use the exact text provided and have the headings listed.
• the three posters must have a common theme. they can be different in back ground but when side by side must look like a set.
• Be suitable for display as A4 and as A2.
Nice to have
• The text needs the be the star, the background needs to draw attention to the poster and the text with out over powering it,
Should not have
• not have photo's of generators or equipment as backgrounds

```html
<!DOCTYPE html>
<html lang="en">
<head>
<meta charset="utf-8">
<title>Tarnwick Drives – Business Goals Posters</title>
<link rel="stylesheet" href="https://fonts.googleapis.com/css2?family=Bungee&family=Rubik:wght@800;900&family=Cinzel:wght@500&display=swap">
<style>
  :root {
    --stage: #000000;
    --paper: #ffffff;
    --ink: #111111;
    --brand-red: #e41e26;
    --heading-yellow: #fff200;
    --icon-grey: #3a3a3a;
    --caption: #f2f2f2;
  }
  * { box-sizing: border-box; margin: 0; padding: 0; }
  html, body {
    width: 1200px; height: 698px; overflow: hidden;
    background: var(--stage);
  }
  .poster-set { position: relative; width: 1200px; height: 698px; }
  .poster {
    position: absolute; top: 72px;
    width: 344px; height: 502px;
    background: var(--paper);
    padding: 12px;
  }
  .poster--quality { left: 41px; }
  .poster--productivity { left: 417px; }
  .poster--safety { left: 792px; }
  .poster__frame {
    height: 100%;
    border: 4px solid var(--ink);
    display: flex; flex-direction: column;
  }
  .poster__head {
    position: relative;
    height: 190px;
    background: var(--paper);
  }
  .brand {
    position: absolute; left: 14px; top: 76px;
    display: flex; align-items: center; gap: 5px;
    font-family: "Rubik", sans-serif; font-weight: 800;
    font-size: 13px; color: var(--ink);
    white-space: nowrap;
  }
  .brand__square {
    width: 12px; height: 12px; background: var(--brand-red);
  }
  .goal-icon {
    position: absolute; right: 14px; top: 16px;
    width: 128px; height: 158px;
    background: radial-gradient(circle at 50% 45%, #5a5a5a 0%, var(--icon-grey) 55%, #1a1a1a 100%);
    border-radius: 18px;
  }
  .goal-icon--circle {
    top: 26px; width: 140px; height: 140px; right: 4px; border-radius: 50%;
  }
  .poster__body {
    flex: 1;
    background: var(--brand-red);
    text-align: center;
    padding-top: 22px;
  }
  .goal-title {
    display: inline-block;
    font-family: "Bungee", sans-serif;
    color: var(--heading-yellow);
    line-height: 1;
    text-shadow: 2px 2px 0 var(--ink), 4px 4px 0 var(--ink), -1px -1px 0 var(--ink), 1px -1px 0 var(--ink), -1px 1px 0 var(--ink);
    transform-origin: center top;
  }
  .goal-title--quality { font-size: 46px; transform: scaleY(1.3); }
  .goal-title--productivity { font-size: 27px; transform: scaleY(1.9); }
  .goal-title--safety { font-size: 54px; transform: scaleY(1.2); }
  .goal-statement {
    margin: 24px auto 0;
    width: 312px;
    font-family: "Rubik", sans-serif; font-weight: 900;
    font-size: 22px; line-height: 30px;
    color: var(--paper);
    white-space: nowrap;
    text-shadow: 1px 1px 0 var(--ink), -1px -1px 0 var(--ink), 1px -1px 0 var(--ink), -1px 1px 0 var(--ink), 2px 2px 0 var(--ink);
  }
  .poster--productivity .goal-statement { margin-top: 26px; }
  .poster--safety .goal-statement { margin-top: 20px; }
  .set-caption {
    position: absolute; left: 0; top: 606px; width: 1200px;
    text-align: center;
    font-family: "Cinzel", serif; font-weight: 500;
    font-size: 28px; color: var(--caption);
    letter-spacing: 1px;
  }
</style>
</head>
<body>
<main class="poster-set">

  <article class="poster poster--quality">
    <div class="poster__frame">
      <header class="poster__head">
        <div class="brand"><span class="brand__square"></span>Tarnwick Drives</div>
        <div class="goal-icon" role="img" aria-label="Award rosette with thumbs-up symbol"></div>
      </header>
      <section class="poster__body">
        <h2 class="goal-title goal-title--quality">QUALITY</h2>
        <p class="goal-statement">We will have pride<br>and ownership of<br>every product and<br>service delivered to<br>our customers.</p>
      </section>
    </div>
  </article>

  <article class="poster poster--productivity">
    <div class="poster__frame">
      <header class="poster__head">
        <div class="brand"><span class="brand__square"></span>Tarnwick Drives</div>
        <div class="goal-icon" role="img" aria-label="Gear with circuit lines radiating outward"></div>
      </header>
      <section class="poster__body">
        <h2 class="goal-title goal-title--productivity">PRODUCTIVITY</h2>
        <p class="goal-statement">We will put<br>the customer's<br>expectations<br>first and ensure our<br>team is empowered<br>to do so.</p>
      </section>
    </div>
  </article>

  <article class="poster poster--safety">
    <div class="poster__frame">
      <header class="poster__head">
        <div class="brand"><span class="brand__square"></span>Tarnwick Drives</div>
        <div class="goal-icon goal-icon--circle" role="img" aria-label="Hard hat inside a black circle"></div>
      </header>
      <section class="poster__body">
        <h2 class="goal-title goal-title--safety">SAFETY</h2>
        <p class="goal-statement">We will shift our<br>culture to ensure<br>safety is our first<br>thought on<br>every job.</p>
      </section>
    </div>
  </article>

  <p class="set-caption">A4 SIZE EACH</p>
</main>
</body>
</html>
```